Quorvel Landing page redesign

We are looking for a landing page redesign before we officially launch. We want to incorporate the information already on the site at www.Quorvel-example.com landing page but make it more inviting. There needs to be a sign up section along with clearly stating what we do. Having a place for sample profiles and linking to our blog and podcast is option. More information about all we will be doing is at Quorvel is on the landing page and also on the blog.

Target Market(s)

35 years old and up.

Coding

Coded - Design and coding required

Number of Pages Required

1 page

Requirements
Must have
• The top bar and the bottom bar (with the privacy policy, etc)
• Sign in/up section.
• I don't want to give to much here because I want designers to be creative.
Nice to have
• Prefer not to have a landing page that requires a lot of scrolling at all.

```html
<!DOCTYPE html>
<html lang="en">
<head>
<meta charset="UTF-8">
<title>Quorvel</title>
<link rel="stylesheet" href="https://fonts.googleapis.com/css2?family=Nunito+Sans:wght@300;400;600;700&display=swap">
<style>
  :root {
    --page-bg: #555555;
    --white: #ffffff;
    --orange: #ef8a43;
    --orange-panel: rgba(240, 137, 62, 0.94);
    --teal: #25e8c8;
    --text-dark: #4a4a4a;
    --field-text: #333333;
  }
  * { box-sizing: border-box; margin: 0; padding: 0; }
  html, body {
    width: 1200px;
    height: 737px;
    overflow: hidden;
    background: var(--page-bg);
    font-family: "Nunito Sans", Arial, sans-serif;
  }
  .canvas { position: relative; width: 1200px; height: 737px; }

  .brand { position: absolute; color: var(--white); font-weight: 400; }
  .site-header .brand { left: 117px; top: 40px; font-size: 22px; line-height: 28px; }
  .site-footer .brand { left: 117px; top: 684px; font-size: 15px; line-height: 18px; }

  .main-nav { position: absolute; top: 46px; left: 0; width: 100%; }
  .main-nav a {
    position: absolute; color: var(--white); text-decoration: none;
    font-size: 13.5px; font-weight: 600; letter-spacing: 0.04em;
  }
  .nav-blog { left: 880px; }
  .nav-podcast { left: 941px; }
  .nav-login { left: 1056px; }

  .hero {
    position: absolute; left: 86px; top: 93px; width: 1029px; height: 396px;
  }
  .hero-art {
    position: absolute; inset: 0;
    background:
      radial-gradient(circle at 15% 30%, #f5b98c 0%, transparent 35%),
      radial-gradient(circle at 85% 25%, #f3a9c3 0%, transparent 35%),
      radial-gradient(circle at 80% 80%, #f7c84a 0%, transparent 30%),
      radial-gradient(circle at 20% 80%, #7fc8e0 0%, transparent 35%),
      linear-gradient(120deg, #8fe0da 0%, #f2b48e 50%, #a6e3df 100%);
  }
  .signup-panel {
    position: absolute; left: 274px; top: 45px; width: 480px; height: 289px;
    background: var(--orange-panel); color: var(--white); text-align: center;
  }
  .signup-title { margin-top: 37px; font-size: 25px; font-weight: 600; letter-spacing: 0.03em; }
  .signup-lede { margin-top: 10px; font-size: 13.6px; font-weight: 600; line-height: 20px; }
  .signup-label { margin-top: 40px; font-size: 17px; font-weight: 600; letter-spacing: 0.05em; }
  .signup-form { position: absolute; left: 81px; top: 194px; display: flex; }
  .signup-email {
    width: 219px; height: 49px; border: none; padding: 0 13px;
    font-family: inherit; font-size: 13px; letter-spacing: 0.03em; color: var(--field-text);
    background: var(--white);
  }
  .signup-email::placeholder { color: var(--field-text); }
  .signup-submit {
    margin-left: 17px; width: 119px; height: 45px; border: 1px solid rgba(255,255,255,0.7);
    background: var(--teal); color: #1f4f48; font-family: inherit;
    font-size: 12.5px; font-weight: 600; letter-spacing: 0.08em;
  }

  .features {
    position: absolute; left: 86px; top: 489px; width: 1029px; height: 178px;
    background: var(--white);
  }
  .feature { position: absolute; top: 44px; text-align: center; }
  .feature-title { font-size: 24px; font-weight: 400; color: var(--orange); line-height: 30px; }
  .feature-text { margin-top: 9px; font-size: 14.5px; color: var(--text-dark); line-height: 20.5px; }
  .feature-divider { position: absolute; top: 41px; width: 1px; height: 87px; background: var(--orange); }
  .f-create { left: 68px; width: 130px; }
  .f-memorialize { left: 246px; width: 156px; }
  .f-share { left: 443px; width: 150px; }
  .f-control { left: 637px; width: 120px; }
  .f-noads { left: 797px; width: 180px; }

  .footer-links {
    position: absolute; right: 123px; top: 685px; display: flex; gap: 15px;
    list-style: none; font-size: 10.5px; font-weight: 600;
  }
  .footer-links a, .footer-links span { color: var(--white); text-decoration: none; }
</style>
</head>
<body>
<div class="canvas">
  <header class="site-header">
    <div class="brand">Quorvel</div>
    <nav class="main-nav">
      <a class="nav-blog" href="#">BLOG</a>
      <a class="nav-podcast" href="#">PODCAST</a>
      <a class="nav-login" href="#">LOGIN</a>
    </nav>
  </header>

  <section class="hero">
    <div class="hero-art" role="img" aria-label="Colourful illustration of a crowd of smiling families hugging one another"></div>
    <div class="signup-panel">
      <h1 class="signup-title">Quorvel Pages</h1>
      <p class="signup-lede">Build multiple Quorvel pages through one account for yourself,<br>your family and to keep loved one's legacies alive.</p>
      <h2 class="signup-label">SIGNUP</h2>
      <form class="signup-form">
        <input class="signup-email" type="email" placeholder="Enter email address">
        <button class="signup-submit" type="button">SUBSCRIBE</button>
      </form>
    </div>
  </section>

  <section class="features">
    <div class="feature f-create"><h3 class="feature-title">Create</h3><p class="feature-text">Create Timelines,<br>Maps, Family Trees</p></div>
    <span class="feature-divider" style="left:226px"></span>
    <div class="feature f-memorialize"><h3 class="feature-title">Memorialize</h3><p class="feature-text">Memorialize<br>Loved Ones</p></div>
    <span class="feature-divider" style="left:421px"></span>
    <div class="feature f-share"><h3 class="feature-title">Share</h3><p class="feature-text">Share Family Stories,<br>History and more</p></div>
    <span class="feature-divider" style="left:618px"></span>
    <div class="feature f-control"><h3 class="feature-title">Control</h3><p class="feature-text">Control<br>Your Privacy</p></div>
    <span class="feature-divider" style="left:775px"></span>
    <div class="feature f-noads"><h3 class="feature-title">No Ads</h3><p class="feature-text">No Ads, No Like Buttons<br>No News Feeds</p></div>
  </section>

  <footer class="site-footer">
    <div class="brand">Quorvel</div>
    <ul class="footer-links">
      <li><a href="#">Privacy Policy</a></li>
      <li><a href="#">Terms of Use</a></li>
      <li><a href="#">Data Tracking</a></li>
      <li><a href="#">Policy</a></li>
      <li><a href="#">Submit Feedback</a></li>
      <li><span>Quorvel © 2017</span></li>
    </ul>
  </footer>
</div>
</body>
</html>
```